Gift Card Design - Suds Harbor Lane

I am needing a design for a standard plastic gift card, (ever so slightly large then a standard rounded edge business card). Name of the business is Suds Harbor Lane. Attached is a file with a poor example, done by an equipment manufacturing firm, that I feel could be much better. Simple, clean and classy with what it is and does along with our name is what I am looking for. Attached also is out logo and source of logo, they don't have to be on the card.

Target Market(s)

Car wash customers in an upscale market.

Industry/Entity Type

Business

Font styles to use
Serif
Other font styles liked:
• whatever you feel, but I do like the font on a Verlance golf ball

Requirements
Must have
• Words anywhere on the card -
• Reloadable Card
• Self Serve Bays & Vacuums.
• Also need name of the business, Suds Harbor Lane.
Nice to have
• Work in Pantone #7483 as there is existing signage with that as a primary color, just trying to tie things together. Attached is my business logo and a picture of the source of the logo, you do not have to use those if you don't want to. I do like clean and classy but am open to creativity, that's why I am submitting this project.
Should not have
• Naked lady pictures

```html
<!DOCTYPE html>
<html lang="en">
<head>
<meta charset="utf-8">
<title>Suds Harbor Lane – Reloadable Card</title>
<link href="https://fonts.googleapis.com/css2?family=Kristi&family=Cormorant+Garamond:wght@500;600&display=swap" rel="stylesheet">
<style>
  :root {
    --page-bg: #ffffff;
    --card-teal: #007381;
    --title-ice: #dcf6f6;
    --text-white: #ffffff;
    --rule-green: #b9c46a;
    --mark-cyan: #3fc4dc;
    --foam-light: #eef3f8;
    --foam-mid: #d3dfeb;
    --foam-deep: #b7c9dc;
  }
  * { margin: 0; padding: 0; box-sizing: border-box; }
  html, body {
    width: 1200px;
    height: 782px;
    overflow: hidden;
    background: var(--page-bg);
  }
  .canvas {
    position: relative;
    width: 1200px;
    height: 782px;
  }
  .gift-card {
    position: absolute;
    left: 40px;
    top: 45px;
    width: 1120px;
    height: 691px;
    border-radius: 18px;
    overflow: hidden;
    background: var(--card-teal);
  }
  .foam-layer {
    position: absolute;
    inset: 0;
    width: 100%;
    height: 100%;
  }
  .card-title {
    position: absolute;
    left: 220px;
    right: 0;
    top: 0;
    text-align: center;
    font-family: "Kristi", cursive;
    font-size: 118px;
    line-height: 1;
    letter-spacing: 4px;
    color: var(--title-ice);
    padding-top: 8px;
  }
  .card-type {
    position: absolute;
    left: 454px;
    width: 464px;
    top: 118px;
    text-align: center;
    font-family: "Cormorant Garamond", serif;
    font-weight: 500;
    font-size: 62px;
    line-height: 1;
    letter-spacing: 3px;
    color: var(--text-white);
    padding-bottom: 10px;
    border-bottom: 2px solid var(--rule-green);
  }
  .card-services {
    position: absolute;
    left: 220px;
    right: 0;
    top: 210px;
    text-align: center;
    font-family: "Cormorant Garamond", serif;
    font-weight: 500;
    font-size: 43px;
    letter-spacing: 5px;
    color: var(--text-white);
  }
  .brand-mark {
    position: absolute;
    left: 470px;
    width: 420px;
    top: 410px;
    display: flex;
    align-items: center;
    justify-content: center;
    gap: 16px;
    font-family: "Cormorant Garamond", serif;
    font-weight: 600;
    font-size: 40px;
    letter-spacing: 3px;
    color: var(--mark-cyan);
    text-transform: uppercase;
  }
  .brand-dot {
    width: 22px;
    height: 22px;
    border-radius: 50%;
    background: var(--mark-cyan);
    flex: none;
  }
</style>
</head>
<body>
<main class="canvas">
  <section class="gift-card">
    <p class="brand-mark"><span class="brand-dot"></span>Suds Harbor Lane</p>
    <svg class="foam-layer" viewBox="0 0 1120 691" role="img" aria-label="Close-up of white soap foam bubbles sweeping around the card edge">
      <defs>
        <radialGradient id="foamGradient" cx="0.2" cy="0.6" r="0.9">
          <stop offset="0" stop-color="var(--foam-light)"/>
          <stop offset="0.6" stop-color="var(--foam-mid)"/>
          <stop offset="1" stop-color="var(--foam-deep)"/>
        </radialGradient>
      </defs>
      <path fill="url(#foamGradient)" d="M0 0 H217 C205 111 244 333 422 500 C578 622 889 578 1120 478 V691 H0 Z"/>
    </svg>
    <h1 class="card-title">Suds Harbor Lane</h1>
    <p class="card-type">Reloadable Card</p>
    <p class="card-services">Self Serve Bays &amp; Vacuums</p>
  </section>
</main>
</body>
</html>
```